Business Card for Brevel Coatings

We need a simple, yet out standing business card for our painting company.

Target Market(s)

wealthy; high-end neighborhoods, and businesses

Industry/Entity Type

Painting

Contact Information for Business Card

Name:
Doran Vask

Email:
d.vask@brevel-coatings.com

Website:
Brevel-coatings.com

Phone Number:
(555) 416-9073

Font styles to use
Serif
Sans Serif

Requirements
Must have
• slogan "making change simple"
Should not have
• A title attached to the name on the card

```html
<!DOCTYPE html>
<html lang="en">
<head>
<meta charset="utf-8">
<title>Brevel Coatings Business Card</title>
<link rel="stylesheet" href="https://fonts.googleapis.com/css2?family=Lato:wght@400;700&display=swap">
<style>
  :root {
    --bg: #e9ebe8;
    --green-deep: #1f5a35;
    --green-mid: #2b7a48;
    --green-panel: #25603a;
    --lime: #8cc63f;
    --lime-soft: #b5dc6e;
    --white: #ffffff;
    --shadow: rgba(0, 0, 0, 0.18);
  }
  * { box-sizing: border-box; margin: 0; padding: 0; }
  html, body {
    width: 1200px;
    height: 898px;
    overflow: hidden;
    background: var(--bg);
    font-family: "Lato", Arial, sans-serif;
  }
  .canvas {
    position: relative;
    width: 1200px;
    height: 898px;
  }
  .card {
    position: absolute;
    width: 580px;
    height: 331px;
    box-shadow: 0 8px 22px var(--shadow);
    overflow: hidden;
  }
  /* front side */
  .card-front {
    left: 310px;
    top: 80px;
    background: radial-gradient(ellipse at 50% 30%, var(--green-mid) 0%, var(--green-deep) 80%);
    color: var(--white);
  }
  .brand {
    position: absolute;
    display: flex;
    align-items: center;
    font-weight: 700;
    text-transform: uppercase;
    white-space: nowrap;
  }
  .brand-dot {
    border-radius: 50%;
    background: var(--lime);
    flex: none;
  }
  .card-front .brand {
    left: 0;
    right: 0;
    top: 112px;
    justify-content: center;
    gap: 14px;
    font-size: 36px;
    letter-spacing: 0.12em;
    color: var(--white);
  }
  .card-front .brand-dot { width: 20px; height: 20px; }
  .slogan {
    position: absolute;
    left: 0;
    right: 0;
    top: 170px;
    text-align: center;
    font-size: 15px;
    letter-spacing: 0.2em;
    color: var(--lime);
  }
  .front-url {
    position: absolute;
    left: 0;
    right: 0;
    bottom: 48px;
    text-align: center;
    font-size: 15px;
    letter-spacing: 0.14em;
  }
  /* back side */
  .card-back {
    left: 350px;
    top: 480px;
    background: var(--white);
  }
  .card-back svg.swoosh {
    position: absolute;
    inset: 0;
  }
  .contact {
    position: absolute;
    left: 40px;
    top: 92px;
    color: var(--white);
  }
  .contact-name {
    font-size: 23px;
    font-weight: 400;
    margin-bottom: 20px;
  }
  .contact-address {
    font-size: 15px;
    line-height: 1.35;
    margin-bottom: 24px;
  }
  .contact-list {
    list-style: none;
    font-size: 15px;
    line-height: 1.55;
  }
  .contact-list li {
    display: flex;
    align-items: center;
    gap: 12px;
  }
  .contact-list svg { flex: none; }
  .card-back .brand {
    left: 372px;
    top: 128px;
    gap: 10px;
    font-size: 24px;
    letter-spacing: 0.1em;
    line-height: 1.15;
    color: var(--green-deep);
  }
  .card-back .brand-dot { width: 14px; height: 14px; }
</style>
</head>
<body>
<main class="canvas">
  <section class="card card-front">
    <div class="brand"><span class="brand-dot"></span>Brevel Coatings</div>
    <p class="slogan">making change simple</p>
    <p class="front-url">www.brevel-coatings.com</p>
  </section>

  <section class="card card-back">
    <svg class="swoosh" width="580" height="331" viewBox="0 0 580 331" aria-hidden="true">
      <path d="M0 0 H320 C270 110 300 250 420 331 H0 Z" fill="var(--green-panel)"/>
      <path d="M320 0 H345 C285 110 320 250 450 331 H420 C300 250 270 110 320 0 Z" fill="var(--lime)"/>
      <path d="M345 0 H362 C305 110 335 240 460 331 H450 C320 250 285 110 345 0 Z" fill="var(--green-panel)"/>
      <path d="M362 0 H372 C318 110 348 235 470 331 H460 C335 240 305 110 362 0 Z" fill="var(--lime-soft)"/>
    </svg>

    <div class="contact">
      <p class="contact-name">Doran Vask</p>
      <p class="contact-address">4180 Mill Crest<br>Dalton TX 75000</p>
      <ul class="contact-list">
        <li>
          <svg width="14" height="14" viewBox="0 0 24 24" aria-label="Phone"><path fill="var(--lime)" d="M6.6 10.8a15 15 0 0 0 6.6 6.6l2.2-2.2c.3-.3.7-.4 1-.2 1.1.4 2.3.6 3.6.6.6 0 1 .4 1 1V20c0 .6-.4 1-1 1A17 17 0 0 1 3 4c0-.6.4-1 1-1h3.5c.6 0 1 .4 1 1 0 1.3.2 2.5.6 3.6.1.3 0 .7-.2 1z"/></svg>
          (555) 416-9073
        </li>
        <li>
          <svg width="14" height="14" viewBox="0 0 24 24" aria-label="Email"><rect x="2" y="5" width="20" height="14" rx="2" fill="var(--lime)"/><path d="M3 6l9 7 9-7" stroke="var(--green-panel)" stroke-width="2" fill="none"/></svg>
          d.vask@brevel-coatings.com
        </li>
        <li>
          <svg width="14" height="14" viewBox="0 0 24 24" aria-label="Website"><circle cx="12" cy="12" r="10" fill="var(--lime)"/><path d="M2 12h20M12 2c3 3 3 17 0 20M12 2c-3 3-3 17 0 20" stroke="var(--green-panel)" stroke-width="1.5" fill="none"/></svg>
          www.brevel-coatings.com
        </li>
      </ul>
    </div>

    <div class="brand"><span class="brand-dot"></span><span>Brevel<br>Coatings</span></div>
  </section>
</main>
</body>
</html>
```